brisk pelts buisness card design

I need a buisness card that has an orange and red outline a side on antelopes head with long horns.I love the one I found on searchly but it has a watermark see below,would it be possible to have something similar?
There is only one other supplier of skins on the sunshine coast ,very expensive and there are a lot of Australian hides.I can supply
a less expensive choice which is extremly different.

Target Market(s)

home owners family stylists bulk buying anniverary wedding gifts

Industry/Entity Type

Searchly

Contact Information for Business Card

BRISK PELTS
EXOTIC HOMEWARES FOR THE MODERN HOME
MIRANDA 0417263948 bellamoor@examplemail.test
imported from Africa no single product the same

Requirements
Must have
• on front BRISK PELTS large either side of logo
red and orange

ethically produced
Nice to have
• I still have to have more pics of gear set up so just one on back
Should not have
• live animals research shows people dont like to look at animal
no running writing

```html
<!DOCTYPE html>
<html lang="en">
<head>
<meta charset="utf-8">
<title>Brisk Pelts – Business Card</title>
<link href="https://fonts.googleapis.com/css2?family=Ubuntu:wght@500;700&family=Arimo&family=PT+Sans+Narrow&display=swap" rel="stylesheet">
<style>
  :root {
    --backdrop: #2b2b2b;
    --card-blush: #e2cbc2;
    --band-maroon: #861a18;
    --band-orange: #e35424;
    --frame-orange: #f06a24;
    --frame-maroon: #7c1a1e;
    --brand-olive: #4a4115;
    --tagline-green: #173a30;
    --accent-rust: #d4502a;
    --ink: #1c1c1c;
    --art-light: #d9c3b9;
    --art-dark: #5a4a44;
  }
  * { margin: 0; padding: 0; box-sizing: border-box; }
  html, body { width: 1200px; height: 1200px; overflow: hidden; }
  body { background: var(--backdrop); position: relative; }

  .business-card {
    position: absolute;
    left: 100px; top: 310px;
    width: 1000px; height: 580px;
    background: var(--card-blush);
    overflow: hidden;
  }
  .top-band {
    position: absolute; left: 0; top: 0;
    width: 100%; height: 52px;
    background: var(--band-maroon);
  }
  .bottom-band {
    position: absolute; left: 0; top: 432px;
    width: 100%; height: 148px;
    background: var(--band-orange);
  }
  .emblem-frame {
    position: absolute; left: 42px; top: 78px;
    width: 270px; height: 368px;
    border: 4px solid var(--frame-orange);
    background: var(--card-blush);
  }
  .emblem-frame-inner {
    position: absolute; inset: 14px;
    border: 3px solid var(--frame-maroon);
    padding: 14px;
  }
  .emblem-art {
    width: 100%; height: 100%;
    background: linear-gradient(160deg, var(--art-light) 0%, var(--art-light) 40%, var(--art-dark) 100%);
  }

  .brand-block {
    position: absolute; left: 400px; top: 128px;
    width: 560px;
  }
  .brand-name {
    font-family: "Ubuntu", sans-serif;
    font-weight: 700;
    font-size: 64px; line-height: 1.05;
    color: var(--brand-olive);
    padding-left: 24px;
  }
  .brand-tagline {
    font-family: "Ubuntu", sans-serif;
    font-weight: 700;
    font-size: 44px; line-height: 1.05;
    color: var(--tagline-green);
    margin-top: 4px;
  }
  .brand-subline {
    font-family: "Ubuntu", sans-serif;
    font-weight: 700;
    font-size: 27px; line-height: 1.2;
    color: var(--accent-rust);
    padding-left: 40px;
  }

  .contact-block {
    position: absolute; left: 420px; top: 292px;
    width: 500px;
    font-family: "Arimo", sans-serif;
    font-style: normal;
    color: var(--ink);
    text-align: center;
  }
  .contact-name { font-size: 36px; line-height: 1.3; }
  .contact-phone { font-size: 28px; line-height: 1.5; }
  .contact-email { font-size: 30px; line-height: 1.4; }

  .origin-note {
    position: absolute; left: 42px; top: 458px;
    font-family: "PT Sans Narrow", sans-serif;
    font-size: 30px; line-height: 1.2;
    color: var(--ink);
  }
</style>
</head>
<body>
  <article class="business-card">
    <div class="top-band"></div>
    <div class="bottom-band"></div>

    <div class="emblem-frame">
      <div class="emblem-frame-inner">
        <div class="emblem-art" role="img" aria-label="Side-on engraved illustration of an antelope head with long curved horns"></div>
      </div>
    </div>

    <header class="brand-block">
      <h1 class="brand-name">Brisk Pelts</h1>
      <p class="brand-tagline">Exotic Homeware</p>
      <p class="brand-subline">For the modern home</p>
    </header>

    <address class="contact-block">
      <p class="contact-name">Miranda</p>
      <p class="contact-phone">041. 726.3948</p>
      <p class="contact-email">bellamoor@examplemail.test</p>
    </address>

    <p class="origin-note">Imported from Africa<br>Each product is one of a kind</p>
  </article>
</body>
</html>
```